HTML Email marketing template for supplement campaign

I want a general template for email marketing in HTML format. I have a product line of supplements that I want to trade out for email marketing campaigns. I will need to use a bottle renderings, hyper links to product landing pages, and campaign literature/call to action. Coupon codes, QR code to product landing page

Target Market(s)

Elderly 50+

Industry/Entity Type

All Natural Supplement pain relief

Colors

Designer to choose colors to be used in the design.

Requirements
Must have
• All-natural formula: Our pain and inflammation relief supplement is made from carefully selected natural ingredients, providing you with a holistic and gentle approach to relieving pain and inflammation. - Powerful anti-inflammatory properties: Packed with potent botanical extracts and natural compounds, our supplement helps reduce inflammation and soothe discomfort, promoting overall well-being. - No harsh chemicals or artificial additives: We believe in providing you with a pure and clean product. Our supplement is free from harsh chemicals, artificial additives, and fillers, ensuring a natural and safe experience. - Enhanced absorption: Our formula is designed to maximize absorption and bioavailability, allowing your body to efficiently utilize the beneficial properties of the ingredients for optimal results. - Supports overall well-being: In addition to pain and inflammation relief, our supplement promotes overall well-being by supporting a healthy inflammatory response, joint health, and a balanced immune system. Higher Quality and more potent than Ease Meridian (TM)
Nice to have
• black and gold theme

```html
<!DOCTYPE html>
<html lang="en">
<head>
<meta charset="utf-8">
<title>Verdora – All-Natural Pain &amp; Inflammation Relief</title>
<link rel="stylesheet" href="https://fonts.googleapis.com/css2?family=Open+Sans:wght@400;600;700&family=Poppins:wght@600&display=swap">
<style>
  :root {
    --black: #000000;
    --white: #ffffff;
    --gold: #d4af25;
    --gold-soft: #c9a26b;
    --yellow: #ffff00;
    --body-gray: #555555;
    --ink: #111111;
  }
  * { margin: 0; padding: 0; box-sizing: border-box; }
  html, body { width: 1200px; height: 3598px; overflow: hidden; }
  body { font-family: "Open Sans", Arial, sans-serif; background: var(--white); position: relative; }
  .abs { position: absolute; }

  .hero { left: 0; top: 0; width: 1200px; height: 699px; background: var(--black); }
  .brand-name { left: 0; width: 1200px; text-align: center; color: var(--gold-soft); font-weight: 400; line-height: 1.2; }
  .brand-dot { width: 14px; height: 14px; border-radius: 50%; background: var(--gold-soft); left: 593px; }
  .hero-dot { top: 105px; }
  .hero-brand { top: 150px; font-size: 46px; letter-spacing: 14px; padding-left: 14px; }
  .hero-title { left: 0; top: 252px; width: 1200px; text-align: center; font-size: 38px; line-height: 42px; font-weight: 400; color: var(--white); }
  .hero-title .hl { color: var(--yellow); font-weight: 700; }
  .hero-rule { left: 415px; top: 408px; width: 374px; height: 1px; background: var(--white); }
  .formula-title { left: 0; top: 438px; width: 1200px; text-align: center; color: var(--yellow); font-weight: 700; font-size: 20px; line-height: 24px; }
  .formula-text { left: 215px; top: 463px; width: 770px; text-align: center; font-size: 20px; line-height: 24px; color: var(--white); }
  .badge { top: 565px; width: 70px; height: 70px; }
  .badge-label { top: 645px; width: 240px; text-align: center; font-family: "Poppins", Arial, sans-serif; font-weight: 600; font-size: 24px; color: var(--white); }

  .bottle { left: 203px; top: 720px; width: 227px; height: 349px; border-radius: 22px; background: linear-gradient(90deg, #0b0b0b, #2b2b2b 45%, #0b0b0b); }
  .btn { display: block; text-align: center; text-decoration: none; border-radius: 4px; font-size: 23px; }
  .btn-shop { left: 204px; top: 1111px; width: 219px; height: 60px; line-height: 60px; background: var(--gold); color: var(--white); }
  .benefits { left: 482px; top: 718px; width: 535px; font-size: 21px; line-height: 25px; color: var(--ink); list-style: disc; padding-left: 20px; }

  .question { left: 170px; top: 1200px; width: 862px; height: 200px; background: var(--black); color: var(--gold); text-align: center; font-size: 47px; line-height: 53px; font-weight: 400; padding-top: 20px; }
  .story { left: 184px; top: 1423px; width: 834px; font-size: 21px; line-height: 31px; color: var(--body-gray); text-align: justify; }
  .story p { margin-bottom: 31px; }
  .story .close { color: #333; font-weight: 700; margin: 0; }
  .story .close-cta { color: var(--gold); font-weight: 700; margin: 0; }
  .story .close-cta span { color: #333; }

  .wellness { left: 0; top: 2249px; width: 1200px; height: 720px; background: var(--gold); }
  .wellness-photo { left: 170px; top: 2287px; width: 862px; height: 483px; background: linear-gradient(120deg, #e9eef1, #cfdde2 45%, #8fb3c4 75%, #2f4f7a); }
  .wellness-title { left: 0; top: 2783px; width: 1200px; text-align: center; font-size: 35px; font-weight: 700; color: var(--ink); }
  .btn-browse { left: 184px; top: 2855px; width: 276px; height: 60px; line-height: 60px; background: var(--black); color: var(--white); }

  .footer { left: 0; top: 2969px; width: 1200px; height: 629px; background: var(--black); }
  .footer-dot { top: 3035px; }
  .footer-brand { top: 3068px; font-size: 36px; letter-spacing: 12px; padding-left: 12px; }
  .site-url { left: 0; top: 3140px; width: 1200px; text-align: center; font-size: 36px; color: var(--white); }
  .foot-rule { left: 184px; width: 834px; height: 1px; background: var(--white); }
  .notice { left: 0; top: 3256px; width: 1200px; text-align: center; font-size: 19px; line-height: 24px; color: var(--white); }
  .foot-link { top: 3366px; width: 240px; text-align: center; font-size: 20px; color: var(--white); text-decoration: none; }
  .foot-link.underlined { text-decoration: underline; }
  .copyright { left: 0; top: 3448px; width: 1200px; text-align: center; font-size: 17px; color: var(--white); }
</style>
</head>
<body>
  <section class="abs hero"></section>
  <div class="abs brand-dot hero-dot"></div>
  <div class="abs brand-name hero-brand">Verdora</div>
  <h1 class="abs hero-title">Introducing our<br><span class="hl">all-natural pain</span> and <span class="hl">inflammation relief</span><br>product!</h1>
  <div class="abs hero-rule"></div>
  <div class="abs formula-title">All-natural formula</div>
  <p class="abs formula-text">Our pain and inflammation relief supplement is made from carefully selected natural ingredients, providing you with a holistic and gentle approach to relieving pain and inflammation.</p>

  <svg class="abs badge" style="left:339px" viewBox="0 0 70 70"><circle cx="35" cy="35" r="32" fill="none" stroke="#fff" stroke-width="3"/><circle cx="35" cy="35" r="22" fill="#fff"/></svg>
  <svg class="abs badge" style="left:577px" viewBox="0 0 70 70"><circle cx="35" cy="35" r="32" fill="none" stroke="#fff" stroke-width="3"/><circle cx="35" cy="35" r="22" fill="#fff"/></svg>
  <svg class="abs badge" style="left:816px" viewBox="0 0 70 70"><circle cx="35" cy="35" r="32" fill="none" stroke="#fff" stroke-width="3"/><circle cx="35" cy="35" r="22" fill="#fff"/></svg>
  <div class="abs badge-label" style="left:254px">100% Organic</div>
  <div class="abs badge-label" style="left:492px">Gluten Free</div>
  <div class="abs badge-label" style="left:731px">Non-GMO</div>

  <div class="abs bottle" role="img" aria-label="Black supplement tub of FLEXA-9 pain and inflammation support"></div>
  <a class="abs btn btn-shop" href="#">Shop Now</a>
  <ul class="abs benefits">
    <li>Powerful anti-inflammatory properties: Packed with potent botanical extracts and natural compounds, our supplement helps reduce inflammation and soothe discomfort, promoting overall well-being.</li>
    <li>No harsh chemicals or artificial additives: We believe in providing you with a pure and clean product. Our supplement is free from harsh chemicals, artificial additives, and fillers, ensuring a natural and safe experience.</li>
    <li>Enhanced absorption: Our formula is designed to maximize absorption and bioavailability, allowing your body to efficiently utilize the beneficial properties of the ingredients for optimal results.</li>
    <li>Supports overall well-being: In addition to pain and inflammation relief, our supplement promotes overall well-being by supporting a healthy inflammatory response, joint health, and a balanced immune system.</li>
  </ul>

  <h2 class="abs question">Are you tired of relying on<br>synthetic medications to manage<br>your pain and inflammation?</h2>
  <div class="abs story">
    <p>Look no further, because we have the perfect solution for you. Our all-natural pain and inflammation relief formula is carefully crafted using only the finest natural ingredients, specifically chosen for their powerful healing properties.</p>
    <p>Say goodbye to discomfort and hello to relief with our product. Designed to target pain and inflammation at its source, our formula works harmoniously with your body's natural processes to provide effective and long-lasting relief.</p>
    <p>We understand the importance of using natural ingredients, which is why we have carefully selected a blend of botanical extracts and essential fish oils known for their anti-inflammatory and analgesic properties. These ingredients work together synergistically to reduce swelling, soothe sore muscles, and alleviate pain without any harsh side effects.</p>
    <p>Our product is not only effective but also safe to use. Free from artificial additives, preservatives, and synthetic chemicals, you can trust that you are giving your body the best care possible.</p>
    <p>Whether you suffer from chronic pain, sports injuries, arthritis, or general inflammation, our all-natural pain and inflammation relief product is here to help. Experience the power of nature and regain control over your well-being.</p>
    <p class="close">Don't let pain hold you back any longer.</p>
    <p class="close-cta">Try our all-natural pain and inflammation relief product today and discover the natural path to a pain-free life<span>.</span></p>
  </div>

  <section class="abs wellness"></section>
  <div class="abs wellness-photo" role="img" aria-label="Smiling senior woman stretching her arms with a physical therapist, an older man exercising behind her"></div>
  <div class="abs wellness-title">Be Healthy</div>
  <a class="abs btn btn-browse" href="#">BROWSE PRODUCTS</a>

  <footer class="abs footer"></footer>
  <div class="abs brand-dot footer-dot"></div>
  <div class="abs brand-name footer-brand">Verdora</div>
  <div class="abs site-url">https://verdoranutrition.com</div>
  <div class="abs foot-rule" style="top:3227px"></div>
  <p class="abs notice">You are receiving this email because you visited our site<br>or asked us about the regular newsletter</p>
  <div class="abs foot-rule" style="top:3336px"></div>
  <a class="abs foot-link" style="left:194px" href="#">Terms and Service</a>
  <a class="abs foot-link underlined" style="left:478px" href="#">Privacy Policy</a>
  <a class="abs foot-link" style="left:768px" href="#">Unsubscribe</a>
  <p class="abs copyright">© 2024 Verdora Nutrition All Rights Reserved.</p>
</body>
</html>
```